High-end construction company needs a business card design

We need a modern looking business card that draws people in, is memorable and looks so good people will want to sick it on their fridges.
On the first side what is needed are:
Logo
My name - Tomas Verbelk
Title - Managing Director
Website - www.kravel.co.uk
Email - tomas@kravel.co.uk
Telephone - 020 5194 6381
Mobile - 07845319027
On the back side was is needed is a list of all the services we provide:
-Kitchen Renovations
-Bathroom Renovations
-House Renovations
-Garage Conversions
-Extensions
-Loft Conversions
-Conservatories
-Carpentry
-Tiling
-Electrical
-Plumbing & Heating
-Bricklaying
-Landscaping
-Decorating
-Plastering
We would like the colours to be the same shades as on the logo with grey or black for the words.
Target Market(s)
Anyone who needs building work done
Contact Information for Business Card
This business card is for a construction company which strives to deliver excellent service and quality.
The look and feel of the card should represent this.
Requirements
Must have
- On the first side what is needed are:
Logo
My name - Tomas Verbelk
Title - Managing Director
Website - www.kravel.co.uk
Email - tomas@kravel.co.uk
Telephone - 020 5194 6381
Mobile - 07845319027
Nice to have
- Cool looking features

```html
<!DOCTYPE html>
<html lang="en">
<head>
<meta charset="utf-8">
<title>Kravel Construction Ltd – Business Card</title>
<link rel="stylesheet" href="https://fonts.googleapis.com/css2?family=Lato:wght@400;700;900&display=swap">
<style>
  :root {
    --backdrop: #3a3431;
    --card-dark: #242424;
    --card-light: #ffffff;
    --brand-green: #4cb034;
    --brand-green-deep: #3a8f2a;
    --text-light: #f2f2f2;
    --text-grey: #555555;
    --text-dark: #333333;
  }
  * { box-sizing: border-box; margin: 0; padding: 0; }
  html, body {
    width: 1200px; height: 847px; overflow: hidden;
    background: var(--backdrop);
    font-family: "Lato", Arial, sans-serif;
  }
  .canvas { position: relative; width: 1200px; height: 847px; }

  .card {
    position: absolute;
    width: 520px; height: 298px;
    border-radius: 4px;
    box-shadow: 0 10px 28px rgba(0,0,0,.45);
    border-bottom: 6px solid var(--brand-green);
    overflow: hidden;
  }

  /* Back side: services */
  .card-back {
    left: 60px; top: 110px;
    background: var(--card-dark);
  }
  .card-back .brand {
    position: absolute; top: 46px; left: 0; right: 0;
    text-align: center; color: var(--brand-green); font-weight: 900;
  }
  .brand-name { display: block; font-size: 46px; letter-spacing: 2px; line-height: 1; }
  .brand-sub { display: block; font-size: 12px; letter-spacing: 4px; margin-top: 6px; }
  .services {
    position: absolute; top: 150px; left: 30px; right: 30px;
    list-style: none; text-align: center;
    color: var(--text-light); font-size: 15px; line-height: 1.75;
  }
  .services .sep { color: var(--brand-green); padding: 0 5px; }

  /* Front side: contact */
  .card-front {
    left: 620px; top: 440px;
    background: var(--card-light);
  }
  .card-front .brand {
    position: absolute; left: 28px; top: 105px; width: 215px;
    text-align: center; color: var(--brand-green); font-weight: 900;
  }
  .card-front .brand-name { font-size: 44px; }
  .card-front .brand-sub { font-size: 11px; letter-spacing: 3px; }
  .divider {
    position: absolute; left: 268px; top: 50px;
    width: 1px; height: 170px; background: var(--brand-green);
  }
  .contact { position: absolute; left: 292px; top: 62px; }
  .person-name { color: var(--brand-green); font-size: 27px; font-weight: 900; }
  .person-title { color: var(--text-grey); font-size: 15px; margin: 2px 0 16px; }
  .contact-list { list-style: none; color: var(--text-dark); font-size: 15px; }
  .contact-list li { display: flex; align-items: center; gap: 10px; line-height: 1.55; }
  .contact-list svg { width: 14px; height: 14px; flex: none; }
  .web-accent { color: var(--brand-green); }
</style>
</head>
<body>
<main class="canvas">

  <section class="card card-back" aria-label="Services side">
    <div class="brand">
      <span class="brand-name">KRAVEL</span>
      <span class="brand-sub">CONSTRUCTION LTD</span>
    </div>
    <ul class="services">
      <li>Kitchen Renovations<span class="sep">|</span>Bathroom Renovations<span class="sep">|</span>House Renovations</li>
      <li>Garage Conversions<span class="sep">|</span>Extensions<span class="sep">|</span>Loft Conversions<span class="sep">|</span>Conservatories</li>
      <li>Carpentry<span class="sep">|</span>Tiling<span class="sep">|</span>Electrical<span class="sep">|</span>Plumbing &amp; Heating</li>
      <li>Bricklaying<span class="sep">|</span>Landscaping<span class="sep">|</span>Decorating<span class="sep">|</span>Plastering</li>
    </ul>
  </section>

  <section class="card card-front" aria-label="Contact side">
    <div class="brand">
      <span class="brand-name">KRAVEL</span>
      <span class="brand-sub">CONSTRUCTION LTD</span>
    </div>
    <div class="divider"></div>
    <div class="contact">
      <h1 class="person-name">Tomas Verbelk</h1>
      <p class="person-title">Managing Director</p>
      <ul class="contact-list">
        <li>
          <svg viewBox="0 0 14 14" aria-hidden="true"><path d="M1 4c0-2 2-3 6-3s6 1 6 3v1H9V3.5H5V5H1zM3 6h8l1 7H2z" fill="var(--brand-green)"/><circle cx="7" cy="9.5" r="1.6" fill="#fff"/></svg>
          020 5194 6381
        </li>
        <li>
          <svg viewBox="0 0 14 14" aria-hidden="true"><rect x="3.5" y="0.5" width="7" height="13" rx="1.5" fill="none" stroke="var(--brand-green)" stroke-width="1.3"/><circle cx="7" cy="11.3" r="0.8" fill="var(--brand-green)"/></svg>
          07845319027
        </li>
        <li>
          <svg viewBox="0 0 14 14" aria-hidden="true"><rect x="0.5" y="2.5" width="13" height="9" fill="var(--brand-green)"/><path d="M0.5 2.5L7 8l6.5-5.5" fill="none" stroke="#fff" stroke-width="1"/></svg>
          tomas@kravel.co.uk
        </li>
        <li>
          <svg viewBox="0 0 14 14" aria-hidden="true"><circle cx="7" cy="7" r="6" fill="var(--brand-green)"/><path d="M1 7h12M7 1c-3 3-3 9 0 12M7 1c3 3 3 9 0 12" fill="none" stroke="#fff" stroke-width="0.8"/></svg>
          <span>www.<span class="web-accent">kravel</span>.co.uk</span>
        </li>
      </ul>
    </div>
  </section>

</main>
</body>
</html>
```